R7M Horizon Business Card Design

We need a business card created for our New Business "R7M Horizon"<br/><br/>The business card design is up to you however the following information must be on the business card:<br/><br/>Front of the business card -<br/>Email :tobyw@r7mhorizon.nz<br/>Mobile: +64 (0) 22 4871 569<br/>Website: www.r7mhorizon.nz<br/>Card Owner Name: Tobias Wrenhall<br/>Company Title: Business Development Manager<br/>Slogan: "The BEST of both worlds". <br/>Logo On the front attached to the design brief<br/><br/>On the back: <br/>Space on the back for 4 more versions of the logo across the bottom of the card indicating different subsidiary brands - R7M Coffee, R7M Arts, R7M ?? (The card will be used for all of these brands - We Will add the extra subsidiary logos to the design once the design is finished (We are a graphics design team). <br/><br/>Other than that we want a premium feeling logo that remains universally usable depending on the business entity that we are using the card for. The use of bright bold colours would be great but we still want the card to feel premium.
Target Market(s)
Gift Design and Manufacturing Companies
Contact Information for Business Card
Front of the business card -
Email :tobyw@r7mhorizon.nz
Mobile: +64 (0) 22 4871 569
Website: www.r7mhorizon.nz
Card Owner Name: Tobias Wrenhall
Company Title: Business Development Manager
Slogan: "The BEST of both worlds".
Logo On the front attached to the design brief

```html
<!DOCTYPE html>
<html lang="en">
<head>
<meta charset="utf-8">
<title>R7M Horizon Business Card</title>
<link href="https://fonts.googleapis.com/css2?family=Open+Sans:wght@400;600;700&display=swap" rel="stylesheet">
<style>
  :root {
    --backdrop: #66abbf;
    --card: #f4f4f4;
    --brand-blue: #2e3192;
    --ink: #222428;
    --shadow: rgba(20, 60, 75, 0.35);
  }
  * { box-sizing: border-box; margin: 0; padding: 0; }
  html, body {
    width: 1200px;
    height: 814px;
    overflow: hidden;
    background: var(--backdrop);
    font-family: "Open Sans", Arial, sans-serif;
  }
  .sheet {
    width: 1200px;
    height: 814px;
    display: flex;
    flex-direction: column;
    align-items: center;
    justify-content: center;
    gap: 40px;
  }
  .card {
    width: 600px;
    height: 343px;
    background: var(--card);
    box-shadow: 0 14px 30px var(--shadow);
    position: relative;
  }
  .brand-name {
    color: var(--brand-blue);
    font-weight: 700;
    letter-spacing: 0.5px;
    white-space: nowrap;
  }

  /* Brand side */
  .card--brand {
    display: flex;
    flex-direction: column;
    align-items: center;
    justify-content: center;
    gap: 26px;
  }
  .card--brand .brand-name { font-size: 38px; line-height: 1.1; }
  .slogan {
    color: var(--ink);
    font-weight: 700;
    font-size: 11px;
    letter-spacing: 3px;
    text-transform: uppercase;
  }

  /* Contact side */
  .card--contact {
    display: flex;
    align-items: center;
    justify-content: center;
    padding: 0 40px;
  }
  .card--contact .brand-name { font-size: 26px; line-height: 1.1; }
  .divider {
    width: 1.5px;
    height: 92px;
    background: var(--brand-blue);
    margin: 0 22px;
    flex: none;
  }
  .owner__name {
    color: var(--brand-blue);
    font-weight: 700;
    font-size: 17px;
    line-height: 1.2;
  }
  .owner__title {
    color: var(--ink);
    font-size: 12.5px;
    margin-bottom: 8px;
  }
  .contact-list { list-style: none; }
  .contact-list li {
    display: flex;
    align-items: center;
    gap: 8px;
    color: var(--ink);
    font-size: 12.5px;
    line-height: 1.55;
    white-space: nowrap;
  }
  .contact-list svg {
    width: 11px;
    height: 11px;
    flex: none;
    fill: none;
    stroke: var(--brand-blue);
    stroke-width: 1.6;
  }
</style>
</head>
<body>
<main class="sheet">
  <section class="card card--brand" aria-label="Card back">
    <p class="brand-name">R7M Horizon</p>
    <p class="slogan">The best of both worlds</p>
  </section>

  <section class="card card--contact" aria-label="Card front">
    <p class="brand-name">R7M Horizon</p>
    <div class="divider"></div>
    <div class="owner">
      <p class="owner__name">Tobias Wrenhall</p>
      <p class="owner__title">Business Development Manager</p>
      <ul class="contact-list">
        <li>
          <svg viewBox="0 0 12 12" aria-hidden="true"><rect x="3" y="0.8" width="6" height="10.4" rx="1"/><line x1="5.3" y1="9.3" x2="6.7" y2="9.3"/></svg>
          +64 (0) 22 4871 569
        </li>
        <li>
          <svg viewBox="0 0 12 12" aria-hidden="true"><rect x="0.8" y="2.5" width="10.4" height="7" rx="0.8"/><polyline points="0.8,2.8 6,6.6 11.2,2.8"/></svg>
          tobyw@r7mhorizon.nz
        </li>
        <li>
          <svg viewBox="0 0 12 12" aria-hidden="true"><circle cx="6" cy="6" r="5"/><ellipse cx="6" cy="6" rx="2.2" ry="5"/><line x1="1" y1="6" x2="11" y2="6"/></svg>
          www.r7mhorizon.nz
        </li>
      </ul>
    </div>
  </section>
</main>
</body>
</html>
```